ZENITH conference Slide Deck

This is a conference for our team that will be 3 days of discussions on how to build our business in the middle of these challenging time. Its a bit of a battle and so we are going with a red and grey/black these although I am open to your interpretation. I will include a few graphics that we have started on to show you the look. But I am just getting started, INSPIRE ME! The screen will be 100' across the front of the room and these decks will show on each side and I will reformat for the middle 1X6 screen as needed. I have the AI file of the logo if you need it. I don't see where to upload it here.

Target Market(s)

our top producers

Industry/Entity Type

Real Estate Agent

Font styles to use
Sans Serif

Colors
ec1f27

Requirements
Must have
• Depth, creativity

```html
<!DOCTYPE html>
<html lang="en">
<head>
<meta charset="utf-8">
<title>ZENITH Conference Slide Deck</title>
<link href="https://fonts.googleapis.com/css2?family=Poppins:wght@300;400;500;600;700;800&display=swap" rel="stylesheet">
<style>
:root{
  --red:#ec1f27;
  --red-deep:#c8101a;
  --ink:#1b1b1d;
  --night:#141518;
  --grey:#8a8a8e;
  --mist:#eeeef1;
  --pale-red:#fbd7d9;
  --hero-blue:#5b6cb8;
  --white:#ffffff;
}
*{box-sizing:border-box;margin:0;padding:0}
html,body{width:684px;height:1200px;overflow:hidden;background:#fff}
body{font-family:'Poppins',Arial,sans-serif;color:var(--ink)}
.stage{position:absolute;left:0;top:0;width:1456px;height:2556px;transform:scale(0.46978);transform-origin:0 0;background:#f3f3f5}
.hero-bg{position:absolute;left:0;top:0;width:1456px;height:600px;background:linear-gradient(115deg,#9ea3b0 0%,#c2c5cd 35%,#e4e5ea 55%,#eeeef1 100%)}
.hero-title{position:absolute;left:86px;top:218px;font-weight:800;font-size:78px;color:var(--hero-blue);letter-spacing:-1px;line-height:1}
.hero-sub{position:absolute;left:238px;top:296px;font-weight:400;font-size:76px;color:#222;line-height:1}
.screen{position:absolute;left:682px;top:103px;width:564px;height:320px;overflow:hidden}
.screen .slide{position:absolute;left:0;top:0;transform:scale(1.2103);transform-origin:0 0}
.slide{position:absolute;width:466px;height:262px;overflow:hidden;background:var(--white)}
.a{position:absolute}
.photo-dark{background:linear-gradient(160deg,#2a2c31 0%,#17181b 45%,#3a3d44 75%,#1e1f23 100%)}
.logo{font-weight:800;color:var(--red);letter-spacing:1px;line-height:1}
.vlogo{position:absolute;writing-mode:vertical-rl;font-weight:800;color:var(--red);font-size:15px;letter-spacing:1px;line-height:1}
.vlogo.up{transform:rotate(180deg)}
.strip{position:absolute;left:0;top:0;width:22px;height:262px;background:#0d0d0e}
.vline{position:absolute;width:1px;background:rgba(255,255,255,.7)}
.redbar{position:absolute;width:2px;background:var(--red)}
.dot{position:absolute;width:8px;height:8px;border:1px solid var(--red);border-radius:50%}
.btn{position:absolute;background:var(--red);color:#fff;font-weight:700;font-size:8px;border-radius:12px;display:flex;align-items:center;justify-content:center}
.t-bold{font-weight:700}
.t-light{font-weight:300}
.tiny{font-size:5px;line-height:1.45;color:#555}
.tiny-w{font-size:5px;line-height:1.45;color:#ddd}
.kicker{font-size:5px;letter-spacing:3px;font-weight:600}
.agenda-item{position:absolute;font-size:7px;color:var(--red)}
.agenda-item::after{content:"";position:absolute;left:0;top:12px;width:10px;height:1px;background:var(--red)}
.grid-box{position:absolute;left:66px;top:48px;width:332px;height:166px;border:1px solid #ddd;border-radius:10px;display:grid;grid-template-columns:repeat(4,1fr);grid-template-rows:1fr 1fr;overflow:hidden}
.grid-box div{border-right:1px solid #777;border-bottom:1px solid #777;padding:16px 8px 0;color:#fff}
.grid-box h4{font-size:7px;font-weight:600;margin-bottom:3px}
.grid-box .hl{background:var(--red)}
.stat{position:absolute;width:120px;text-align:center}
.stat b{display:block;color:var(--red);font-size:18px;font-weight:600}
.partner{position:absolute;width:44px;height:11px;background:#d4d4d8;border-radius:3px}
.card{position:absolute;width:90px;height:95px;border-radius:8px;background:#fff;box-shadow:0 2px 8px rgba(0,0,0,.15);text-align:center;padding:10px 6px 0}
.card h5{font-size:6px;font-weight:600;margin:14px 0 3px}
.card.hl{background:var(--red);color:#fff}
.card .ico{width:10px;height:10px;border:1px solid currentColor;border-radius:2px;margin:0 auto}
.data{position:absolute;left:180px;top:98px;width:275px;border-collapse:collapse;font-size:5px;text-align:center}
.data th{background:#111;color:#fff;font-weight:600;height:20px}
.data th.hl{background:var(--red)}
.data td{height:24px;border-bottom:1px solid #ddd;color:#333}
.data td.hl{background:var(--pale-red)}
.icon-ring{position:absolute;width:34px;height:34px;border-radius:50%;background:var(--red);border:3px solid #f6c9cb}
.check{position:absolute;width:8px;height:8px;background:var(--red);border-radius:1px}
</style>
</head>
<body>
<div class="stage">

  <div class="hero-bg" role="img" aria-label="Crowd of people raising their hands at sunset, softly faded"></div>
  <div class="hero-title">Presentation</div>
  <div class="hero-sub">Deck</div>

  <!-- featured title slide -->
  <div class="screen">
    <div class="slide photo-dark" role="img" aria-label="Dark upward view of glass office towers">
      <div class="a logo" style="left:28px;top:20px;font-size:14px">ZENITH</div>
      <div class="vline" style="left:22px;top:30px;height:210px"></div>
      <div class="vlogo" style="left:438px;top:18px">ZENITH</div>
      <div class="vline" style="left:446px;top:76px;height:126px"></div>
      <div class="dot" style="left:442px;top:210px"></div><div class="dot" style="left:442px;top:222px"></div><div class="dot" style="left:442px;top:234px"></div>
      <div class="a t-bold" style="left:0;width:466px;top:108px;text-align:center;color:#fff;font-size:18px">Here Is A Place To Add</div>
      <div class="a t-light" style="left:0;width:466px;top:131px;text-align:center;color:#fff;font-size:18px">Your Awesome Text</div>
      <div class="btn" style="left:201px;top:178px;width:88px;height:20px">Your Text Here</div>
    </div>
  </div>

  <!-- row 1 -->
  <div class="slide photo-dark" style="left:18px;top:605px" role="img" aria-label="Dark upward view of glass office towers">
    <div class="a logo" style="left:28px;top:22px;font-size:13px">ZENITH</div>
    <div class="vline" style="left:22px;top:30px;height:215px"></div>
    <div class="vlogo" style="left:438px;top:16px">ZENITH</div>
    <div class="vline" style="left:447px;top:74px;height:126px"></div>
    <div class="dot" style="left:443px;top:205px"></div><div class="dot" style="left:443px;top:218px"></div><div class="dot" style="left:443px;top:231px"></div>
    <div class="a t-bold" style="left:0;width:466px;top:106px;text-align:center;color:#fff;font-size:18px">Here Is A Place To Add</div>
    <div class="a t-light" style="left:0;width:466px;top:129px;text-align:center;color:#fff;font-size:18px">Your Awesome Text</div>
    <div class="btn" style="left:190px;top:177px;width:88px;height:20px">Your Text Here</div>
  </div>

  <div class="slide photo-dark" style="left:495px;top:605px" role="img" aria-label="Dark upward view of glass office towers">
    <div class="a logo" style="left:32px;top:60px;font-size:20px">ZENITH</div>
    <div class="vline" style="left:20px;top:100px;height:45px"></div>
    <div class="vline" style="left:20px;top:0;height:25px"></div>
    <div class="vlogo" style="left:438px;top:16px">ZENITH</div>
    <div class="vline" style="left:447px;top:74px;height:126px"></div>
    <div class="dot" style="left:443px;top:205px"></div><div class="dot" style="left:443px;top:218px"></div><div class="dot" style="left:443px;top:231px"></div>
    <div class="a t-bold" style="left:30px;top:100px;color:#fff;font-size:18px">Here Is A Place To Add</div>
    <div class="a t-light" style="left:30px;top:123px;color:#fff;font-size:18px">Your Awesome Text</div>
    <div class="btn" style="left:27px;top:185px;width:88px;height:20px">Your Text Here</div>
  </div>

  <div class="slide photo-dark" style="left:976px;top:605px" role="img" aria-label="Dark upward view of glass office towers">
    <div class="vline" style="left:20px;top:80px;height:20px;width:2px;background:#fff"></div>
    <div class="a t-bold" style="left:38px;top:76px;color:#fff;font-size:18px;font-weight:500">Agenda</div>
    <div class="vlogo" style="left:438px;top:16px">ZENITH</div>
    <div class="vline" style="left:447px;top:74px;height:170px"></div>
    <div class="agenda-item" style="left:42px;top:125px">Opening the summit</div>
    <div class="agenda-item" style="left:42px;top:152px">Market outlook talks</div>
    <div class="agenda-item" style="left:42px;top:178px">Top producer panels</div>
    <div class="agenda-item" style="left:42px;top:205px">Listing growth plans</div>
    <div class="agenda-item" style="left:190px;top:125px">Lead strategy session</div>
    <div class="agenda-item" style="left:190px;top:152px">Pricing in tight times</div>
    <div class="agenda-item" style="left:190px;top:178px">Client trust workshop</div>
    <div class="agenda-item" style="left:190px;top:205px">Team awards dinner</div>
    <div class="agenda-item" style="left:336px;top:125px">Referral engine lab</div>
    <div class="agenda-item" style="left:336px;top:152px">Digital brand review</div>
    <div class="agenda-item" style="left:336px;top:178px">Coaching breakouts</div>
    <div class="agenda-item" style="left:336px;top:205px">Closing keynote talk</div>
  </div>

  <!-- row 2 -->
  <div class="slide photo-dark" style="left:18px;top:882px" role="img" aria-label="Dark background with faint red network lines">
    <div class="redbar" style="left:20px;top:20px;height:24px"></div>
    <div class="vlogo up" style="left:4px;top:205px">ZENITH</div>
    <div class="grid-box">
      <div class="hl"><h4 style="margin-top:10px">Here Is A Place To Add <span style="font-weight:300">Your Awesome Text</span></h4></div>
      <div><h4>Your Text Here</h4><p class="tiny-w">Short notes on the day one sessions and goals ahead.</p></div>
      <div><h4>Your Text Here</h4><p class="tiny-w">Short notes on the day two sessions and goals ahead.</p></div>
      <div><h4>Your Text Here</h4><p class="tiny-w">Short notes on the day three sessions and goals ahead.</p></div>
      <div><h4>Your Text Here</h4><p class="tiny-w">Keynote themes for our top producers this year.</p></div>
      <div><h4>Your Text Here</h4><p class="tiny-w">Breakout topics for growing listings in hard times.</p></div>
      <div><h4>Your Text Here</h4><p class="tiny-w">Panel notes on pricing, trust and client care.</p></div>
      <div><h4>Your Text Here</h4><p class="tiny-w">Closing plans to carry the energy back home.</p></div>
    </div>
  </div>

  <div class="slide" style="left:495px;top:882px">
    <div class="a photo-dark" style="left:0;top:0;width:156px;height:262px;background:linear-gradient(100deg,#0c0c0d 0%,#2b2b2e 55%,#121213 100%)" role="img" aria-label="Portrait of the presenter in dark tones"></div>
    <div class="vlogo up" style="left:4px;top:205px">ZENITH</div>
    <div class="a" style="left:156px;top:0;width:126px;height:262px;background:#8b8b8d"></div>
    <div class="a t-bold" style="left:175px;top:48px;color:#fff;font-size:10px;line-height:1.3;font-weight:600">Presenter<br>Name</div>
    <svg class="a" style="left:176px;top:112px" width="8" height="8" viewBox="0 0 8 8"><path d="M1 1 L3 1 L3.6 2.8 L2.6 3.6 Q3.4 5 4.6 5.6 L5.4 4.6 L7.2 5.2 L7.2 7 Q3 7.4 1 1Z" fill="#fff"/></svg>
    <div class="a" style="left:196px;top:113px;color:#fff;font-size:5.5px">00(000)0000</div>
    <svg class="a" style="left:176px;top:148px" width="9" height="7" viewBox="0 0 9 7"><rect x="0.5" y="0.5" width="8" height="6" fill="#fff"/><path d="M0.5 0.5 L4.5 4 L8.5 0.5" stroke="#8b8b8d" fill="none"/></svg>
    <div class="a" style="left:196px;top:148px;color:#fff;font-size:5.5px">hello@zenithmeet.co</div>
    <svg class="a" style="left:176px;top:184px" width="8" height="8" viewBox="0 0 8 8"><circle cx="4" cy="4" r="3.5" stroke="#fff" fill="none"/><path d="M0.5 4 H7.5 M4 0.5 V7.5" stroke="#fff"/></svg>
    <div class="a" style="left:196px;top:185px;color:#fff;font-size:5.5px">www.zenithmeet.co</div>
    <div class="a kicker" style="left:309px;top:42px;color:#333">SUB TITLE GOES HERE</div>
    <div class="a t-bold" style="left:309px;top:52px;font-size:10.5px;line-height:1.15">Add Awesome<br>Title Here</div>
    <p class="a tiny" style="left:309px;top:88px;width:128px;text-align:justify">Three days together to sharpen how we win listings, keep clients close and lead our markets through uncertain times. Every session is built for top producers who want practical tools, honest numbers and fresh ideas they can use on Monday morning. Bring your questions, your best wins and your toughest deals, and leave with a plan to grow.</p>
  </div>

  <div class="slide" style="left:976px;top:882px">
    <div class="strip"></div>
    <div class="vlogo up" style="left:4px;top:205px">ZENITH</div>
    <div class="a logo" style="left:0;width:466px;top:60px;text-align:center;font-size:20px;padding-left:22px">ZENITH</div>
    <div class="a" style="left:90px;top:92px;width:292px;height:64px;background:var(--red);border-radius:4px;box-shadow:8px 12px 14px rgba(0,0,0,.18);text-align:center;color:#fff;padding-top:10px">
      <div class="t-bold" style="font-size:15px;line-height:1.35">Here Is A Place To Add</div>
      <div class="t-light" style="font-size:15px;line-height:1.35">Your Awesome Quote</div>
    </div>
  </div>

  <!-- row 3 -->
  <div class="slide" style="left:18px;top:1167px">
    <div class="strip"></div>
    <div class="vlogo up" style="left:4px;top:205px">ZENITH</div>
    <div class="a" style="left:62px;top:44px;width:336px;height:186px;background:var(--red);border-radius:30px"></div>
    <div class="a t-bold" style="left:91px;top:88px;color:#fff;font-size:15px;line-height:1.55">Here Is A Place<br>To Add Your<br>Awesome Text<br>Or A Quote</div>
    <div class="a" style="left:256px;top:70px;width:180px;height:134px;background:linear-gradient(150deg,#b9dde9 0%,#3f7f95 45%,#143845 100%);box-shadow:4px 6px 12px rgba(0,0,0,.25)" role="img" aria-label="Glass skyscraper seen from below"></div>
  </div>

  <div class="slide" style="left:495px;top:1167px">
    <div class="redbar" style="left:22px;top:20px;height:26px"></div>
    <div class="vlogo up" style="left:4px;top:205px">ZENITH</div>
    <div class="a" style="left:152px;top:0;width:314px;height:168px;background:linear-gradient(135deg,#6b4a34 0%,#9c7a5e 40%,#d9d4cc 70%,#5a4334 100%)" role="img" aria-label="Team working on laptops around a wooden table, seen from above"></div>
    <div class="a" style="left:70px;top:95px;width:125px;height:95px;background:var(--red);border-radius:8px;color:#fff;padding:12px 12px 0">
      <div class="t-bold" style="font-size:9px">01.</div>
      <div class="t-bold" style="font-size:5.5px;margin-top:8px">Your Text Here</div>
      <p style="font-size:4px;line-height:1.4;margin-top:4px;color:#fde">Short note on the first key idea we will share together on day one.</p>
    </div>
    <div class="a" style="left:90px;top:203px;font-size:16.5px;font-weight:400;white-space:nowrap">Your <span style="color:var(--red);font-weight:600">Awesome</span> Text Here</div>
  </div>

  <div class="slide" style="left:976px;top:1167px">
    <div class="a" style="left:16px;top:150px;font-size:82px;font-weight:800;color:var(--pale-red);letter-spacing:2px;line-height:1">ZENITH</div>
    <div class="strip"></div>
    <div class="vlogo up" style="left:4px;top:205px">ZENITH</div>
    <div class="a t-bold" style="left:40px;top:90px;font-size:16px;font-weight:600">Heading</div>
    <div class="a" style="left:40px;top:112px;font-size:10px">And Text Slide</div>
    <p class="a tiny" style="left:263px;top:72px;width:152px;font-size:3.6px">Our top producers face a shifting market, rising rates and cautious buyers. This summit is our chance to trade what works, test new ideas and return home with stronger habits, clearer goals and a team that knows it can lead the way.</p>
    <p class="a tiny" style="left:263px;top:128px;width:152px;font-size:3.6px">Each session pairs real results with hands on planning, so every agent leaves with steps to take this month. We will cover pricing, listings, referrals and client care, and share the wins that carried us through the hardest seasons so far.</p>
  </div>

  <!-- row 4 -->
  <div class="slide" style="left:18px;top:1445px">
    <div class="redbar" style="left:20px;top:0;height:30px"></div>
    <div class="vlogo up" style="left:4px;top:205px">ZENITH</div>
    <div class="a kicker" style="left:34px;top:50px;color:var(--red)">SUB TITLE GOES HERE</div>
    <div class="a" style="left:34px;top:58px;font-size:10.5px;line-height:1.15">Add Awesome Title<br>Or A Quote</div>
    <div class="a" style="left:35px;top:128px;width:305px;height:112px;background:var(--mist);border-radius:12px"></div>
    <div class="a t-bold" style="left:60px;top:152px;font-size:4.5px;color:var(--red)">Your Text Here</div>
    <p class="a tiny" style="left:60px;top:162px;width:80px;font-size:3.6px">Short note on a key win from our team this past year.</p>
    <div class="a t-bold" style="left:170px;top:152px;font-size:4.5px;color:var(--red)">Your Text Here</div>
    <p class="a tiny" style="left:170px;top:162px;width:80px;font-size:3.6px">Short note on a key goal for our team this coming year.</p>
    <div class="a" style="left:243px;top:30px;width:189px;height:120px;background:linear-gradient(135deg,#5d6f86 0%,#9fa9b7 50%,#e6e8ec 100%)" role="img" aria-label="House keys resting on a signed contract"></div>
    <div class="a" style="left:278px;top:135px;width:177px;height:64px;background:var(--red);border-radius:6px;color:#fff;padding:10px 14px 0">
      <div style="font-size:7px"><b style="font-size:8.5px;font-weight:600">2020</b>&nbsp; Lorem Ipsum Dollar</div>
      <p style="font-size:3.4px;line-height:1.4;margin-top:5px">A year that tested every agent, and a team that rose to meet it again.</p>
    </div>
  </div>

  <div class="slide" style="left:495px;top:1445px">
    <div class="a" style="left:0;top:0;width:466px;height:102px;background:linear-gradient(100deg,#d51a22 0%,#c41118 60%,#a90d14 100%)" role="img" aria-label="Red tinted photo of people at a meeting table"></div>
    <div class="strip" style="background:#0d0d0e"></div>
    <div class="vlogo up" style="left:4px;top:205px">ZENITH</div>
    <div class="a kicker" style="left:44px;top:34px;color:#fff">SUB TITLE GOES HERE</div>
    <div class="a t-bold" style="left:44px;top:42px;color:#fff;font-size:11px;line-height:1.2;font-weight:600">Add Awesome Title Here<br>Or A Quote</div>
    <p class="a tiny" style="left:44px;top:122px;width:178px;font-size:3.8px;text-align:justify">The past year asked more of us than any before it. Buyers paused, sellers waited and every deal took more care. Yet our top producers kept showing up, kept learning and kept closing. This summit is built on that spirit. We will look hard at what the numbers say, share the tools that helped us hold our ground and set clear targets for the next twelve months. Come ready to listen, to teach and to push one another further than we could go alone.</p>
    <p class="a tiny" style="left:246px;top:122px;width:186px;font-size:3.8px;text-align:justify">Each day opens with a keynote and closes with hands on breakouts led by our strongest agents. You will map your own listing plan, refine your client follow up and sharpen the way you talk about price in a cautious market. Between sessions there is time to connect, compare notes and celebrate the people who carried our brand through a tough season. We leave with one shared goal and the confidence to chase it together.</p>
  </div>

  <div class="slide" style="left:976px;top:1445px">
    <div class="redbar" style="left:22px;top:55px;height:28px"></div>
    <div class="a" style="left:0;width:466px;top:62px;text-align:center;font-size:18px;font-weight:600">Your <span style="color:var(--red)">awesome</span> text here</div>
    <p class="a tiny" style="left:60px;top:96px;width:346px;text-align:center;font-size:4px">Our team has grown through every market shift, and these numbers show how far our top producers have carried us. They are a starting point for the goals we will set together across the next three days of this summit.</p>
    <div class="stat" style="left:43px;top:150px"><b>1M</b><p class="tiny" style="color:#999;font-size:4.5px">Total sales volume closed by our top producers last year</p></div>
    <div class="stat" style="left:178px;top:150px"><b>2021</b><p class="tiny" style="color:#999;font-size:4.5px">The year our team set its best closing record so far</p></div>
    <div class="stat" style="left:313px;top:150px"><b>150+</b><p class="tiny" style="color:#999;font-size:4.5px">Agents joining us for three days of focused work</p></div>
  </div>

  <!-- row 5 -->
  <div class="slide" style="left:18px;top:1723px">
    <div class="strip"></div>
    <div class="vlogo up" style="left:4px;top:205px">ZENITH</div>
    <div class="a t-bold" style="left:60px;top:24px;width:360px;text-align:center;font-size:12px;line-height:1.5;font-weight:600">Here is A Place To Mention Or Say A Couple Words About Your Partners Or Competitors</div>
    <div class="a" style="left:22px;top:98px;width:444px;height:126px;background:#f3f3f5"></div>
    <div class="partner" style="left:72px;top:114px"></div><div class="partner" style="left:180px;top:116px;width:20px"></div><div class="partner" style="left:285px;top:116px"></div><div class="partner" style="left:405px;top:116px;width:30px"></div>
    <div class="partner" style="left:72px;top:154px;width:34px"></div><div class="partner" style="left:180px;top:154px;width:34px"></div><div class="partner" style="left:290px;top:154px"></div><div class="partner" style="left:390px;top:154px"></div>
    <div class="partner" style="left:68px;top:192px;width:40px"></div><div class="partner" style="left:180px;top:192px;width:32px"></div><div class="partner" style="left:290px;top:190px;height:14px"></div><div class="partner" style="left:408px;top:192px;width:32px"></div>
  </div>

  <div class="slide" style="left:495px;top:1723px">
    <div class="a" style="left:0;top:0;width:466px;height:168px;background:linear-gradient(180deg,#9a9da3 0%,#c9cbcf 55%,#ffffff 100%)" role="img" aria-label="City skyline seen through tall office windows"></div>
    <div class="a" style="left:222px;top:142px;width:18px;height:18px;border-radius:50%;background:var(--red);color:#fff;font-size:12px;font-weight:700;text-align:center;line-height:20px">“</div>
    <p class="a tiny" style="left:70px;top:172px;width:326px;text-align:center;font-size:4.8px;color:#333">We do not wait for the market to turn. We show up, we serve our clients and we build the kind of trust that lasts through every season, good or hard.</p>
    <div class="a t-bold" style="left:0;width:466px;top:198px;text-align:center;font-size:4.8px;color:var(--red)">Your Name</div>
  </div>

  <div class="slide" style="left:976px;top:1723px">
    <div class="strip"></div>
    <div class="vlogo up" style="left:4px;top:205px">ZENITH</div>
    <div class="a" style="left:22px;top:0;width:168px;height:262px;background:linear-gradient(160deg,#c9b59c 0%,#8e8070 40%,#dcdfe3 75%,#a9adb4 100%)" role="img" aria-label="Hands typing on a laptop beside a coffee mug"></div>
    <div class="a" style="left:208px;top:50px;font-size:11px">Heading And Text Slide</div>
    <p class="a tiny" style="left:208px;top:82px;width:218px;font-size:3.8px">A short note on the projects our agents will bring to the table, and how each one ties back to the bigger goals we set for this year.</p>
    <div class="card hl" style="left:135px;top:140px"><div class="ico"></div><h5>Project name</h5><p style="font-size:3.4px;line-height:1.4">Notes on our first team project for the year ahead.</p></div>
    <div class="card" style="left:235px;top:140px"><div class="ico" style="color:var(--red)"></div><h5>Project name</h5><p class="tiny" style="font-size:3.4px">Notes on our second team project for the year ahead.</p></div>
    <div class="card" style="left:335px;top:140px"><div class="ico" style="color:var(--red)"></div><h5>Project name</h5><p class="tiny" style="font-size:3.4px">Notes on our third team project for the year ahead.</p></div>
  </div>

  <!-- row 6 -->
  <div class="slide" style="left:18px;top:2001px;background:#2a2a2c">
    <div class="strip" style="background:#0d0d0e"></div>
    <div class="vlogo up" style="left:4px;top:205px">ZENITH</div>
    <div class="a t-bold" style="left:46px;top:22px;color:#fff;font-size:18px">Your Text Goes Here</div>
    <div class="a" style="left:46px;top:46px;color:#fff;font-size:6.5px">Sub title goes here</div>
    <div class="a" style="left:160px;top:84px;width:306px;height:178px;background:#fff;border-top-left-radius:16px"></div>
    <div class="a" style="left:44px;top:100px;color:#fff;font-size:5px;font-weight:600">Project name</div>
    <p class="a tiny-w" style="left:44px;top:108px;width:100px;font-size:3.8px">A short note on this project and what it means for our team.</p>
    <div class="a" style="left:44px;top:153px;color:#fff;font-size:5px;font-weight:600">Project name</div>
    <p class="a tiny-w" style="left:44px;top:161px;width:100px;font-size:3.8px">A short note on this project and what it means for our team.</p>
    <div class="a" style="left:44px;top:206px;color:#fff;font-size:5px;font-weight:600">Project name</div>
    <p class="a tiny-w" style="left:44px;top:214px;width:100px;font-size:3.8px">A short note on this project and what it means for our team.</p>
    <table class="data">
      <tr><th>Text</th><th>Text</th><th>Text</th><th>Text</th><th class="hl">Text</th><th>Text</th></tr>
      <tr><td>Data</td><td>Data</td><td>Data</td><td>Data</td><td class="hl">Data</td><td>Data</td></tr>
      <tr><td>Data</td><td>Data</td><td>Data</td><td>Data</td><td class="hl">Data</td><td>Data</td></tr>
      <tr><td>Data</td><td>Data</td><td>Data</td><td>Data</td><td class="hl">Data</td><td>Data</td></tr>
      <tr><td>Data</td><td>Data</td><td>Data</td><td>Data</td><td class="hl">Data</td><td>Data</td></tr>
      <tr><td>Data</td><td>Data</td><td>Data</td><td>Data</td><td class="hl">Data</td><td>Data</td></tr>
    </table>
  </div>

  <div class="slide" style="left:495px;top:2001px">
    <div class="redbar" style="left:22px;top:20px;height:26px"></div>
    <div class="vlogo up" style="left:4px;top:205px">ZENITH</div>
    <div class="a" style="left:24px;top:0;width:253px;height:262px;background:linear-gradient(180deg,#2c333c 0%,#3f4650 45%,#1a1c20 100%)" role="img" aria-label="City skyline at dusk"></div>
    <div class="a t-bold" style="left:42px;top:118px;color:#fff;font-size:20px">Your Text</div>
    <div class="a" style="left:42px;top:142px;color:#fff;font-size:6.5px">Sub title goes here</div>
    <div class="redbar" style="left:44px;top:153px;width:10px;height:1px"></div>
    <div class="icon-ring" style="left:258px;top:30px"></div>
    <div class="icon-ring" style="left:258px;top:112px"></div>
    <div class="icon-ring" style="left:258px;top:192px"></div>
    <div class="a t-bold" style="left:320px;top:30px;font-size:4.8px;color:var(--red)">Your Text Here</div>
    <p class="a tiny" style="left:320px;top:40px;width:112px;font-size:3.8px">A short note on this topic and the steps our team will take.</p>
    <div class="a t-bold" style="left:320px;top:112px;font-size:4.8px;color:var(--red)">Your Text Here</div>
    <p class="a tiny" style="left:320px;top:122px;width:112px;font-size:3.8px">A short note on this topic and the steps our team will take.</p>
    <div class="a t-bold" style="left:320px;top:192px;font-size:4.8px;color:var(--red)">Your Text Here</div>
    <p class="a tiny" style="left:320px;top:202px;width:112px;font-size:3.8px">A short note on this topic and the steps our team will take.</p>
  </div>

  <div class="slide" style="left:976px;top:2001px">
    <div class="redbar" style="left:22px;top:20px;height:24px"></div>
    <div class="vlogo up" style="left:4px;top:205px">ZENITH</div>
    <div class="a" style="left:35px;top:22px;font-size:11px">Add Awesome Title Here</div>
    <div class="a kicker" style="left:35px;top:38px;color:var(--red)">SUB TITLE GOES HERE</div>
    <svg class="a" style="left:40px;top:70px" width="160" height="165" viewBox="0 0 160 165">
      <polygon points="68,5 52,48 88,48" fill="#ec1f27"/>
      <ellipse cx="70" cy="48" rx="18" ry="4" fill="#b0121a"/>
      <polygon points="48,56 92,56 112,98 28,98" fill="#9b9b9f"/>
      <ellipse cx="70" cy="98" rx="42" ry="6" fill="#6e6e72"/>
      <polygon points="22,108 118,108 140,150 0,150" fill="#2a2a2c"/>
      <ellipse cx="70" cy="150" rx="70" ry="8" fill="#111"/>
      <line x1="72" y1="30" x2="150" y2="30" stroke="#888" stroke-width="0.6"/><circle cx="150" cy="30" r="1.5" fill="none" stroke="#555" stroke-width="0.6"/>
      <line x1="72" y1="78" x2="150" y2="78" stroke="#888" stroke-width="0.6"/><circle cx="150" cy="78" r="1.5" fill="none" stroke="#555" stroke-width="0.6"/>
      <line x1="72" y1="126" x2="150" y2="126" stroke="#888" stroke-width="0.6"/><circle cx="150" cy="126" r="1.5" fill="none" stroke="#555" stroke-width="0.6"/>
    </svg>
    <div class="a t-bold" style="left:205px;top:90px;font-size:4.6px">Lorem ipsum dolor sit</div>
    <p class="a tiny" style="left:205px;top:98px;width:228px;font-size:3.6px">A short note on the first level of our plan and the results we expect from it this year.</p>
    <div class="a t-bold" style="left:205px;top:134px;font-size:4.6px">Lorem ipsum dolor sit</div>
    <p class="a tiny" style="left:205px;top:142px;width:228px;font-size:3.6px">A short note on the second level of our plan and the results we expect from it this year.</p>
    <div class="a t-bold" style="left:205px;top:182px;font-size:4.6px">Lorem ipsum dolor sit</div>
    <p class="a tiny" style="left:205px;top:190px;width:228px;font-size:3.6px">A short note on the third level of our plan and the results we expect from it this year.</p>
  </div>

  <!-- row 7 -->
  <div class="slide" style="left:18px;top:2280px">
    <div class="redbar" style="left:20px;top:22px;height:24px"></div>
    <div class="vlogo up" style="left:4px;top:205px">ZENITH</div>
    <div class="a" style="left:35px;top:22px;font-size:11px">Add Awesome Title Here</div>
    <div class="a kicker" style="left:35px;top:38px;color:var(--red)">SUB TITLE GOES HERE</div>
    <svg class="a" style="left:64px;top:84px" width="118" height="118" viewBox="0 0 118 118">
      <circle cx="59" cy="59" r="50" fill="#fff" stroke="#8a8a8e" stroke-width="16"/>
      <circle cx="59" cy="59" r="50" fill="none" stroke="#ec1f27" stroke-width="16" stroke-dasharray="226.2 314.2" transform="rotate(-90 59 59)"/>
      <circle cx="59" cy="59" r="40" fill="#fff"/>
      <text x="59" y="66" text-anchor="middle" font-family="Poppins, sans-serif" font-size="18" fill="#222">72%</text>
    </svg>
    <div class="check" style="left:244px;top:96px"></div>
    <p class="a tiny" style="left:262px;top:94px;width:170px;font-size:3.6px">A short note on the first target our team will meet before the next summit.</p>
    <div class="check" style="left:244px;top:140px"></div>
    <p class="a tiny" style="left:262px;top:138px;width:170px;font-size:3.6px">A short note on the second target our team will meet before the next summit.</p>
    <div class="check" style="left:244px;top:182px"></div>
    <p class="a tiny" style="left:262px;top:180px;width:170px;font-size:3.6px">A short note on the third target our team will meet before the next summit.</p>
  </div>

  <div class="slide" style="left:495px;top:2280px">
    <div class="a logo" style="left:42px;top:18px;font-size:13px">ZENITH</div>
    <div class="vline" style="left:22px;top:170px;height:75px;background:#333"></div>
    <div class="a" style="left:42px;top:40px;width:380px;height:180px;background:linear-gradient(135deg,#6f7074 0%,#b9babd 50%,#7d7e82 100%)" role="img" aria-label="Grey steel and glass roof structure"></div>
    <div class="a t-bold" style="left:42px;width:380px;top:104px;text-align:center;color:#fff;font-size:22px;font-weight:800;letter-spacing:.5px">THANK YOU</div>
    <div class="a t-bold" style="left:42px;width:380px;top:130px;text-align:center;color:#fff;font-size:12px;font-weight:700">FOR WATCHING</div>
    <div class="vlogo" style="left:436px;top:16px">ZENITH</div>
    <div class="vline" style="left:443px;top:74px;height:120px;background:#333"></div>
    <div class="dot" style="left:439px;top:203px"></div><div class="dot" style="left:439px;top:216px"></div><div class="dot" style="left:439px;top:229px"></div>
  </div>

  <div class="slide photo-dark" style="left:976px;top:2280px;background:linear-gradient(180deg,#1f2d3e 0%,#141b24 60%,#0c0f14 100%)" role="img" aria-label="Night city skyline showing through large letters">
    <div class="a" style="left:0;width:466px;top:70px;text-align:center;font-size:86px;font-weight:800;color:#7d93ad;letter-spacing:1px;line-height:1">ZENITH</div>
  </div>

</div>
</body>
</html>
```